Card design for orthopaedic surgeons working as The Brindlewood Orthopaedic Centre

Business cards, letterhead

Colors

Designer to choose colors to be used in the design.

Requirements
Must have
• Late addition.
• Cards letterhead must have logos of
• Corvane Federated Institute of Surgeons
• Meridale Orthopaedic Society
Nice to have
• Back of card to have space for appointment time to be added by hand and some blank space for writing incidental other notes.

```html
<!DOCTYPE html>
<html lang="en">
<head>
<meta charset="utf-8">
<title>The Brindlewood Orthopaedic Centre – Cards</title>
<link rel="stylesheet" href="https://fonts.googleapis.com/css2?family=Roboto:wght@400;500;700&display=swap">
<style>
  :root {
    --backdrop: #b9b9b9;
    --card: #ffffff;
    --sky: #5aaee2;
    --navy: #0f2c44;
    --deep: #04324b;
  }
  * { box-sizing: border-box; margin: 0; padding: 0; }
  html, body { width: 1172px; height: 1200px; overflow: hidden; }
  body {
    background: var(--backdrop);
    font-family: "Roboto", Arial, sans-serif;
    color: var(--navy);
    position: relative;
  }
  .card {
    position: absolute;
    left: 214px;
    width: 744px;
    height: 428px;
    background: var(--card);
    border-radius: 24px;
    overflow: hidden;
  }
  .card--appointment { top: 122px; }
  .card--contact { top: 645px; }

  .brand-name {
    font-size: 29px;
    font-weight: 400;
    color: var(--navy);
    letter-spacing: -0.3px;
    white-space: nowrap;
  }
  .card--appointment .brand-name {
    position: absolute; top: 84px; left: 0; right: 0; text-align: center;
  }
  .appointment-title {
    position: absolute; top: 142px; left: 0; right: 0; text-align: center;
    color: var(--sky); font-weight: 700; font-size: 26px; letter-spacing: 0.2px;
  }
  .fill-row {
    position: absolute; left: 52px; right: 55px;
    display: flex; align-items: baseline; font-size: 21px; white-space: nowrap;
  }
  .fill-row--patient { top: 206px; }
  .fill-row--when { top: 278px; }
  .leader { flex: 1; border-bottom: 2px dotted var(--navy); margin: 0 2px 5px; }
  .leader--date { margin-right: 12px; }
  .leader--time { margin-left: 8px; }
  .weekdays {
    position: absolute; top: 350px; left: 52px; right: 52px;
    display: flex; justify-content: space-between; font-size: 21px; color: var(--sky);
  }
  .weekday { display: flex; align-items: center; gap: 9px; }
  .tick-box { width: 20px; height: 20px; border: 2px solid var(--navy); }

  .card--contact .brand-name { position: absolute; top: 86px; left: 27px; }
  .doctor-name {
    position: absolute; top: 138px; right: 26px;
    color: var(--sky); font-weight: 700; font-size: 29px;
  }
  .accent-bar {
    position: absolute; top: 143px; right: 0; width: 12px; height: 54px; background: var(--sky);
  }
  .rule {
    position: absolute; top: 186px; left: 27px; width: 474px; height: 2px; background: var(--sky);
  }
  .doctor-role {
    position: absolute; top: 175px; right: 26px; font-size: 20px;
  }
  .address { position: absolute; top: 225px; left: 25px; font-size: 20px; line-height: 25px; }
  .contacts { position: absolute; top: 295px; left: 25px; list-style: none; font-size: 20px; }
  .contacts li { display: flex; align-items: center; gap: 8px; height: 25.5px; }
  .contacts svg { width: 16px; height: 16px; fill: var(--sky); }
  .wave { position: absolute; left: 0; bottom: 0; width: 744px; height: 66px; }
</style>
</head>
<body>
  <section class="card card--appointment">
    <div class="brand-name">The Brindlewood Orthopaedic Centre</div>
    <h2 class="appointment-title">YOUR NEXT APPOINTMENT</h2>
    <div class="fill-row fill-row--patient"><span class="leader"></span><span>has an appointment</span></div>
    <div class="fill-row fill-row--when">
      <span>Date:</span><span class="leader leader--date"></span>
      <span>Time:</span><span class="leader leader--time"></span><span>AM/PM</span>
    </div>
    <div class="weekdays">
      <span class="weekday">Sun <span class="tick-box"></span></span>
      <span class="weekday">Mon <span class="tick-box"></span></span>
      <span class="weekday">Tue <span class="tick-box"></span></span>
      <span class="weekday">Wed <span class="tick-box"></span></span>
      <span class="weekday">Thu <span class="tick-box"></span></span>
      <span class="weekday">Fri <span class="tick-box"></span></span>
      <span class="weekday">Sat <span class="tick-box"></span></span>
    </div>
  </section>

  <section class="card card--contact">
    <div class="brand-name">The Brindlewood Orthopaedic Centre</div>
    <h1 class="doctor-name">Dr. Halden Pryce</h1>
    <span class="accent-bar"></span>
    <span class="rule"></span>
    <p class="doctor-role">Orthopaedic Specialist</p>
    <p class="address">P.O. Box: 48213, Tallow Lane<br>Ashcombe, United Kingdom</p>
    <ul class="contacts">
      <li><svg viewBox="0 0 16 16"><path d="M3 1l3 3-1.5 2c1 2 3 4 5 5l2-1.5 3 3-2 2C6 14 2 10 1 3z"/></svg>622-555-0147</li>
      <li><svg viewBox="0 0 16 16"><path d="M1 3h14v10H1z M2 4l6 5 6-5" /></svg>info@brindlewoodortho.com</li>
      <li><svg viewBox="0 0 16 16"><circle cx="8" cy="8" r="7"/></svg>www.brindlewoodortho.com</li>
    </ul>
    <svg class="wave" viewBox="0 0 744 66" preserveAspectRatio="none" aria-hidden="true">
      <path d="M0 20 C120 56 300 52 470 30 C590 16 690 28 744 56 L744 66 L0 66 Z" fill="var(--deep)"/>
      <path d="M0 20 C120 50 300 44 460 24 C580 10 680 16 744 44 C680 22 580 18 470 32 C300 52 120 56 0 24 Z" fill="var(--sky)"/>
      <path d="M6 22 C130 54 300 50 470 28 C590 12 690 22 740 48" fill="none" stroke="#fff" stroke-width="3"/>
    </svg>
  </section>
</body>
</html>
```